Stylish Business Cards Wanted

- DOUBLE SIDED Design Required -

High end, edgy cards for a corporate and personal stylist. Must include logo,
Name: Belinda Forsey
Title: Director and Stylist
telephone : +61 8 8217 4592
email: belinda@thegarbledger.example
website: thegarbledger.example
Tag: Corporate Workwear & Uniform Specialist | Personal Stylist
Would like nice icons for telephone, email, website

Target Market(s)

Businesses wanting stylish uniforms, people wanting stylish wardrobes

Industry/Entity Type

Corporate Workwear Stylist

Contact Information for Business Card

I would like black, white and gold foiling incorporated in the design - possibly a touch of the other colours on my branding guide attached Name: Belinda Forsey Title: Director and Stylist telephone : +61 8 8217 4592 email: belinda@thegarbledger.example website: thegarbledger.example Tag: Corporate Workwear & Uniform Specialist | Personal Stylist Would like nice icons for telephone, email, website

Font styles to use
Other font styles liked:
• Raleway

Colors

Designer to choose colors to be used in the design.

Requirements
Must have
• Gold foil accents

```html
<!DOCTYPE html>
<html lang="en">
<head>
<meta charset="utf-8">
<title>The Garb Ledger – Business Cards</title>
<link href="https://fonts.googleapis.com/css2?family=Roboto+Condensed:wght@300;400&display=swap" rel="stylesheet">
<style>
  :root {
    --backdrop: #2a2a2c;
    --card-white: #f4f4f4;
    --card-black: #161616;
    --ink: #3a3a3a;
    --ink-dark: #1c1c1c;
    --gold: #e8b84a;
    --navy: #1f2f5a;
    --rule: #3b4050;
    --white: #ffffff;
  }
  * { margin: 0; padding: 0; box-sizing: border-box; }
  html, body {
    width: 1200px; height: 900px; overflow: hidden;
    background: var(--backdrop);
    font-family: "Roboto Condensed", Arial, sans-serif;
  }
  .stage {
    width: 1200px; height: 900px;
    display: flex; align-items: center; justify-content: center; gap: 50px;
  }
  .card {
    width: 540px; height: 300px; position: relative;
    box-shadow: 0 14px 30px rgba(0,0,0,.45);
  }
  /* Front */
  .card-front { background: var(--card-white); color: var(--ink); }
  .person { position: absolute; left: 34px; top: 30px; }
  .person-name { font-weight: 300; font-size: 40px; color: var(--gold); line-height: 1; }
  .person-title { font-size: 15px; color: var(--ink-dark); margin-top: 6px; }
  .name-rule {
    position: absolute; left: 186px; right: 0; top: 104px;
    border-top: 1.5px solid var(--rule);
  }
  .brand-front {
    position: absolute; right: 30px; top: 34px;
    display: flex; align-items: center; gap: 10px;
  }
  .brand-name { font-weight: 400; font-size: 30px; letter-spacing: .5px; color: var(--ink-dark); }
  .brand-mark { width: 16px; height: 16px; background: var(--ink-dark); }
  .contacts {
    position: absolute; left: 150px; top: 118px;
    font-size: 13px; line-height: 1.45; color: var(--ink);
  }
  .social { display: flex; gap: 8px; margin-top: 6px; }
  .social span { width: 18px; height: 18px; border-radius: 3px; background: var(--navy); }
  .tagline {
    position: absolute; left: 34px; bottom: 26px;
    font-size: 15px; font-weight: 300; color: var(--ink); text-transform: uppercase;
  }
  /* Back */
  .card-back {
    background: var(--card-black);
    display: flex; align-items: center; justify-content: center; gap: 14px;
  }
  .card-back .brand-name { color: var(--white); font-size: 44px; }
  .card-back .brand-mark { width: 22px; height: 22px; background: var(--gold); }
</style>
</head>
<body>
<main class="stage">
  <section class="card card-front" aria-label="Business card front">
    <div class="person">
      <p class="person-name">Belinda Forsey</p>
      <p class="person-title">Director and Stylist</p>
    </div>
    <div class="brand-front">
      <span class="brand-mark"></span>
      <span class="brand-name">The Garb Ledger</span>
    </div>
    <div class="name-rule"></div>
    <div class="contacts">
      <p>Email: belinda@thegarbledger.example</p>
      <p>www.thegarbledger.example</p>
      <p>Telephone : +61 8 8217 4592</p>
      <div class="social" aria-label="Social links">
        <span></span><span></span><span></span><span></span>
      </div>
    </div>
    <p class="tagline">Corporate Workwear | Uniform Specialist | Personal Stylist</p>
  </section>

  <section class="card card-back" aria-label="Business card back">
    <span class="brand-mark"></span>
    <span class="brand-name">The Garb Ledger</span>
  </section>
</main>
</body>
</html>
```